Publishing House

Amber Heron
Exotic, they weave silk out of nowhere. Blessed with a keen sense. Sophisticated discernment. Fearsome reputation. Powerful, but do not harm. Unless, you really needle them. Believe in continuous improvement. A young tarantula may shed its exoskeleton periodically in order to grow, a process called molting : several times a year as a part of the maturation process.
White. The colour pristine. Everything pure. Blemish-free. We feel for the writer. We want to infuse spurt of purity into publishing.
We, at Amber Heron Publishing, are here to question the status-quo, to provide a fresh, invigorating platform for writers to reach their art to their readership via processes that are transparent, impartial and non-discriminatory, and a level of transparency that will set new benchmarks in the world of publishing.
We bring to you new concepts in the areas of editing, proof-reading and cover-designing. Our suite of marketing services targets new, and web-based methods as well as traditional methods.
It is time the writer got his or her due!

I have attached our logo also

Industry/Entity Type

House

```html
<!DOCTYPE html>
<html lang="en">
<head>
<meta charset="utf-8">
<title>Amber Heron – Cover Design</title>
<link rel="stylesheet" href="https://fonts.googleapis.com/css2?family=Open+Sans:wght@400;600&display=swap">
<style>
  :root {
    --page-bg: #e9ebee;
    --amber-light: #f3d9a4;
    --amber-mid: #d9a85a;
    --amber-deep: #b07a32;
    --ink-brown: #4a2b0c;
    --shelf-light: #e8d3b8;
    --shelf-dark: #8a6a4e;
    --frame-white: #ffffff;
    --frame-line: #c9ccd3;
    --ink-black: #111111;
  }
  * { margin: 0; padding: 0; box-sizing: border-box; }
  html, body { width: 1200px; height: 718px; overflow: hidden; }
  body {
    background: var(--page-bg);
    font-family: "Open Sans", Arial, sans-serif;
    position: relative;
  }
  .cover {
    position: absolute;
    left: 20px; top: 113px;
    width: 1160px; height: 425px;
    overflow: hidden;
    background:
      radial-gradient(ellipse at 30% 15%, var(--amber-light) 0%, transparent 55%),
      linear-gradient(100deg, var(--amber-mid) 0%, var(--amber-light) 35%, #f0dcc0 60%, var(--shelf-light) 100%);
  }
  .cover-ornament {
    position: absolute;
    left: 242px; top: 68px;
    width: 292px; height: 115px;
    border-radius: 50%;
    background: radial-gradient(ellipse at center, #fbeccb 0%, rgba(243,217,164,0.6) 50%, transparent 75%);
  }
  .cover-bookshelf {
    position: absolute;
    left: 665px; top: 0;
    width: 495px; height: 425px;
    background: linear-gradient(90deg, rgba(232,211,184,0) 0%, var(--shelf-light) 25%, #c9a98a 60%, var(--shelf-dark) 100%);
  }
  .cover-reader {
    position: absolute;
    left: 964px; top: 0;
    width: 196px; height: 425px;
    background: linear-gradient(180deg, #3a3533 0%, #7a2838 35%, #2f3f5e 60%, #2a3550 100%);
    opacity: 0.85;
  }
  .cover-text {
    position: absolute;
    color: var(--ink-brown);
    white-space: nowrap;
    line-height: 1.2;
  }
  .brand-name { left: 291px; top: 206px; font-size: 30px; }
  .tagline { left: 291px; top: 260px; font-size: 35px; }
  .address { left: 291px; font-size: 20px; }
  .address-1 { top: 311px; }
  .address-2 { top: 341px; }
  .website { left: 287px; top: 380px; font-size: 23px; font-weight: 600; }

  .profile-frame {
    position: absolute;
    left: 51px; top: 378px;
    width: 231px; height: 231px;
    background: var(--frame-white);
    border: 1px solid var(--frame-line);
    border-radius: 3px;
    padding: 7px;
  }
  .profile-art {
    position: relative;
    width: 100%; height: 100%;
    overflow: hidden;
    background:
      radial-gradient(ellipse at 70% 30%, var(--amber-light) 0%, transparent 60%),
      linear-gradient(135deg, var(--amber-mid) 0%, var(--amber-light) 55%, var(--amber-deep) 100%);
  }
  .profile-ornament {
    position: absolute;
    left: 20px; top: 40px;
    width: 177px; height: 75px;
    border-radius: 50%;
    background: radial-gradient(ellipse at center, #fbeccb 0%, rgba(243,217,164,0.5) 55%, transparent 75%);
  }
  .profile-name {
    position: absolute;
    left: 0; right: 0; top: 140px;
    text-align: center;
    font-size: 23px;
    color: var(--ink-black);
    white-space: nowrap;
  }
</style>
</head>
<body>
  <section class="cover">
    <div class="cover-ornament" role="img" aria-label="Golden ornamental flourish with radiating silk lines"></div>
    <div class="cover-bookshelf" role="img" aria-label="Photograph of bookshelves filled with books"></div>
    <div class="cover-reader" role="img" aria-label="Photograph of a person in a leather jacket reading a book, shown from the shoulders down"></div>
    <p class="cover-text brand-name">Amber Heron</p>
    <p class="cover-text tagline">Complete Book Publisher Solutions</p>
    <p class="cover-text address address-1">Address Line Here</p>
    <p class="cover-text address address-2">Address Line Here</p>
    <p class="cover-text website">Our Website : www.amberheronbooks.com</p>
  </section>

  <div class="profile-frame">
    <div class="profile-art">
      <div class="profile-ornament" role="img" aria-label="Golden ornamental flourish"></div>
      <p class="profile-name">Amber Heron</p>
    </div>
  </div>
</body>
</html>
```